LSCo Wholesale Flyer

I need a wholesaler flyer/letter put together. I've provided copy and a range of photos for the designer to use. The flyer needs to match the same colour pallet and style of larkfieldseedhouseco.com.au.

It will be used to send to new potenial retailers so needs to look smick.

```html
<!DOCTYPE html>
<html lang="en">
<head>
<meta charset="utf-8">
<title>LSCo Wholesale Flyer</title>
<link rel="stylesheet" href="https://fonts.googleapis.com/css2?family=Poppins:wght@300;400;500;600;700&display=swap">
<style>
:root{
  --stage:#666666;
  --paper:#dbd6d2;
  --black:#050505;
  --brown:#3c2409;
  --brown-dark:#271507;
  --cream:#f3e5d3;
  --white:#ffffff;
  --ink:#1b120a;
  --photo-top:#2a1b10;
  --photo-mid:#8a5a2c;
  --photo-low:#d9cbb8;
}
*{box-sizing:border-box;margin:0;padding:0}
html,body{width:1200px;height:972px;overflow:hidden}
body{background:var(--stage);font-family:'Poppins',sans-serif;color:var(--ink);position:relative}

.page{position:absolute;width:494px;height:700px;background:var(--paper);overflow:hidden}
.page--front{left:86px;top:136px}
.page--back{left:620px;top:136px}

/* front: story */
.story{position:absolute;left:0;top:0;width:494px;height:286px;background:var(--black);color:var(--white)}
.brand-name{position:absolute;left:36px;top:36px;font-weight:300;font-size:14.5px;line-height:14px;letter-spacing:.3px;text-transform:uppercase;text-align:center;width:112px}
.story-title{position:absolute;left:36px;top:94px;font-weight:500;font-size:10.5px;letter-spacing:3.6px}
.story-copy{position:absolute;left:36px;top:113px;width:232px;font-size:4.7px;line-height:6px;font-weight:400}
.story-copy p{margin-bottom:5.4px}
.signoff{position:absolute;left:36px;top:256px;width:66px;height:11px;background:linear-gradient(90deg,#3a3a3a,#1a1a1a);border-radius:2px}
.story-photo{position:absolute;left:291px;top:32px;width:166px;height:236px;border-radius:83px 83px 0 0;
  background:radial-gradient(circle at 40% 62%,#f0a54a 0,#9a5a22 14%,transparent 34%),linear-gradient(180deg,var(--photo-top) 0%,var(--photo-mid) 52%,var(--photo-low) 100%)}
.story-arch{position:absolute;left:283px;top:24px;width:182px;height:244px;border:1px solid #6b6b6b;border-bottom:none;border-radius:91px 91px 0 0}

/* tables */
.col-heads{position:absolute;display:flex;gap:3px}
.col-head{height:100%;border-radius:12px 12px 0 0;color:var(--white);font-weight:600;font-size:4.8px;line-height:5.4px;text-transform:uppercase;display:flex;align-items:center;justify-content:center;text-align:center}
.col-head--black{background:var(--black)}
.col-head--brown{background:var(--brown-dark)}
.section-title{position:absolute;font-weight:600;font-size:7px;letter-spacing:2.4px;text-transform:uppercase;text-align:center}
.price-table{position:absolute;border-collapse:separate;border-spacing:2px;table-layout:fixed;font-size:6px;font-weight:500}
.price-table td{background:var(--white);padding:0 0 0 6px;white-space:nowrap;overflow:hidden}
.price-table td.item{background:var(--brown);color:var(--white);font-weight:600;white-space:normal;line-height:7px}
.price-table td.item--alt{background:var(--brown-dark)}
.price-table td.size-dark{background:var(--brown);color:var(--white);padding-left:8px}
.price-table td.size-light{background:var(--cream);color:var(--ink);padding-left:8px}
.price-table td.size-white{background:var(--white);padding-left:8px}
.price-table td.num{padding-left:14px}
.price-table td.merged{text-align:center;padding:0}
.price-table td.merged--cream{background:var(--cream)}

.candle-table{left:34px;top:344px}
.candle-table tr{height:11.5px}
.candle-table td.item{font-size:6.4px;line-height:7.6px;padding:0 30px 0 18px}

.back-table tr{height:17px}
.back-table td.item{font-size:5.4px;line-height:6px;padding:0 46px 0 12px}
.back-table td.size-white{line-height:6px;white-space:normal}

.contact{position:absolute;left:0;bottom:0;width:494px;height:61px;background:var(--black);color:var(--white);font-size:6.8px;font-weight:600;display:flex;align-items:flex-start;justify-content:center;gap:5px;padding-top:14px}
.phone-pill{background:var(--cream);color:var(--ink);border-radius:8px;padding:2px 6px;margin-top:-3px;font-size:7px}
.mail{display:inline-flex;align-items:center;gap:4px}
</style>
</head>
<body>

<section class="page page--front">
  <header class="story">
    <div class="brand-name">Larkfield<br>Seedhouse<br>Co.</div>
    <h1 class="story-title">OUR STORY</h1>
    <div class="story-copy">
      <p>Larkfield Seedhouse Co. is a small, family-owned business based on our property, Hollowbrook Farm, in historic Larkfield, Tasmania. Since 2014, we've been creating Tasmanian botanical products that reflect the beauty and simplicity of where we live.</p>
      <p>We handcraft our candles, diffusers, room mists and body products in small batches on the farm. Each product begins with natural ingredients that we grow ourselves or source locally when we can, like calendula, chamomile, rose, rosemary, Tasmanian blue gum and organic Tasmanian seaweed.</p>
      <p>Our candles are poured by hand using natural soy wax and cotton wicks. Their scents are inspired by the Tasmanian landscape. Our diffusers and room mists are blended slowly to create a clean, steady fragrance. And our soaps and body products are created using artisanal methods and botanicals known for their soothing properties.</p>
      <p>Larkfield's history shapes everything we do at LSCo. The village's heritage streets remind us to take our time, keep things simple and make products that feel honest and meaningful.</p>
      <p>We minimise single-use plastics and create with care for people and the planet. And we are proudly cruelty free.</p>
      <p>Thank you for being part of our journey</p>
    </div>
    <div class="signoff" role="img" aria-label="Handwritten sign-off from Nora and Tom"></div>
    <div class="story-arch"></div>
    <div class="story-photo" role="img" aria-label="Photograph of a lit amber jar candle on a set dinner table with dried flowers"></div>
  </header>

  <div class="col-heads" style="left:40px;top:294px;height:40px">
    <div class="col-head col-head--black" style="width:123px">Item</div>
    <div class="col-head col-head--brown" style="width:75px">Size</div>
    <div class="col-head col-head--black" style="width:51px">Wholesale<br>price<br>ex GST</div>
    <div class="col-head col-head--brown" style="width:57px">RRP</div>
    <div class="col-head col-head--black" style="width:56px">Quantity<br>required</div>
    <div class="col-head col-head--brown" style="width:45px">Quantity<br>supplied<br>(office use<br>only)</div>
  </div>
  <div class="section-title" style="left:200px;top:336px;width:130px">Candle range</div>

  <table class="price-table candle-table">
    <colgroup><col style="width:126px"><col style="width:74px"><col style="width:50px"><col style="width:57px"><col style="width:56px"><col style="width:56px"></colgroup>
    <tr><td class="item" rowspan="3">Wild Highland Moorland</td><td class="size-dark">Large</td><td class="num">$35.00</td><td class="num">$62.00</td><td></td><td></td></tr>
    <tr><td class="size-dark">Medium</td><td class="num">$23.00</td><td class="num">$42.00</td><td></td><td></td></tr>
    <tr><td class="size-dark">Small</td><td class="num">$17.00</td><td class="num">$30.00</td><td></td><td></td></tr>
    <tr><td class="item item--alt" rowspan="3">Mountain Pepperleaf and Wild Blackcurrant</td><td class="size-light">Large</td><td class="num">$35.00</td><td class="num">$62.00</td><td></td><td></td></tr>
    <tr><td class="size-white">Medium</td><td class="num">$23.00</td><td class="num">$42.00</td><td></td><td></td></tr>
    <tr><td class="size-light">Small</td><td class="num">$17.00</td><td class="num">$30.00</td><td></td><td></td></tr>
    <tr><td class="item" rowspan="3">Southern Shoreline</td><td class="size-dark">Large</td><td class="num">$35.00</td><td class="num">$62.00</td><td></td><td></td></tr>
    <tr><td class="size-dark">Medium</td><td class="num">$23.00</td><td class="num">$42.00</td><td></td><td></td></tr>
    <tr><td class="size-dark">Small</td><td class="num">$17.00</td><td class="num">$30.00</td><td></td><td></td></tr>
    <tr><td class="item item--alt" rowspan="3">Lavender Meadow</td><td class="size-light">Large</td><td class="num">$35.00</td><td class="num">$62.00</td><td></td><td></td></tr>
    <tr><td class="size-white">Medium</td><td class="num">$23.00</td><td class="num">$42.00</td><td></td><td></td></tr>
    <tr><td class="size-light">Small</td><td class="num">$17.00</td><td class="num">$30.00</td><td></td><td></td></tr>
    <tr><td class="item" rowspan="3">Alpine Frost</td><td class="size-dark">Large</td><td class="num">$35.00</td><td class="num">$62.00</td><td></td><td></td></tr>
    <tr><td class="size-dark">Medium</td><td class="num">$23.00</td><td class="num">$42.00</td><td></td><td></td></tr>
    <tr><td class="size-dark">Small</td><td class="num">$17.00</td><td class="num">$30.00</td><td></td><td></td></tr>
    <tr><td class="item item--alt" rowspan="3">Hearthside Ember</td><td class="size-light">Large</td><td class="num">$35.00</td><td class="num">$62.00</td><td></td><td></td></tr>
    <tr><td class="size-white">Medium</td><td class="num">$23.00</td><td class="num">$42.00</td><td></td><td></td></tr>
    <tr><td class="size-light">Small</td><td class="num">$17.00</td><td class="num">$30.00</td><td></td><td></td></tr>
    <tr><td class="item" rowspan="3">Silver Cedar</td><td class="size-dark">Large</td><td class="num">$35.00</td><td class="num">$62.00</td><td></td><td></td></tr>
    <tr><td class="size-dark">Medium</td><td class="num">$23.00</td><td class="num">$42.00</td><td></td><td></td></tr>
    <tr><td class="size-dark">Small</td><td class="num">$17.00</td><td class="num">$30.00</td><td></td><td></td></tr>
    <tr><td class="item item--alt" rowspan="3">Christmas (seasonal)</td><td class="size-light">Large</td><td class="num">$35.00</td><td class="num">$62.00</td><td></td><td></td></tr>
    <tr><td class="size-white">Medium</td><td class="num">$23.00</td><td class="num">$42.00</td><td></td><td></td></tr>
    <tr><td class="size-light">Small</td><td class="num">$17.00</td><td class="num">$30.00</td><td></td><td></td></tr>
  </table>
</section>

<section class="page page--back">
  <div class="col-heads" style="left:59px;top:38px;height:32px">
    <div class="col-head col-head--black" style="width:134px">Item</div>
    <div class="col-head col-head--brown" style="width:62px">Size</div>
    <div class="col-head col-head--black" style="width:42px">Wholesale<br>price<br>ex GST</div>
    <div class="col-head col-head--brown" style="width:47px">RRP</div>
    <div class="col-head col-head--black" style="width:47px">Quantity<br>required</div>
    <div class="col-head col-head--brown" style="width:37px">Quantity<br>supplied<br>(office use<br>only)</div>
  </div>

  <div class="section-title" style="left:160px;top:74px;width:180px">Soap and body wash</div>
  <table class="price-table back-table" style="left:54px;top:84px">
    <colgroup><col style="width:138px"><col style="width:62px"><col style="width:44px"><col style="width:48px"><col style="width:48px"><col style="width:36px"></colgroup>
    <tr><td class="item">Silver Cedar</td><td class="size-white">120g</td><td class="num">$6.00</td><td class="num">$11.00</td><td></td><td></td></tr>
    <tr><td class="item item--alt">Mountain Pepperleaf and Wild Blackcurrant</td><td class="size-white">120g</td><td class="num">$6.00</td><td class="num">$11.00</td><td></td><td></td></tr>
    <tr><td class="item">Highland Moorland</td><td class="size-white">120g</td><td class="num">$6.00</td><td class="num">$11.00</td><td></td><td></td></tr>
    <tr><td class="item item--alt">Southern Shoreline</td><td class="size-white">120g</td><td class="num">$6.00</td><td class="num">$11.00</td><td></td><td></td></tr>
    <tr><td class="item">Hand and Body Wash</td><td class="size-white">500ml</td><td class="num">$22.00</td><td class="num">$40.00</td><td></td><td></td></tr>
    <tr><td class="item item--alt">Hand and Body Wash Refill</td><td class="size-white">500ml</td><td class="num">$17.50</td><td class="num">$35.00</td><td></td><td></td></tr>
  </table>

  <div class="section-title" style="left:160px;top:203px;width:180px">Diffuser range</div>
  <table class="price-table back-table" style="left:54px;top:213px">
    <colgroup><col style="width:138px"><col style="width:62px"><col style="width:44px"><col style="width:48px"><col style="width:48px"><col style="width:36px"></colgroup>
    <tr><td class="item">Wild Highland Moorland</td><td class="size-white">100ml</td><td class="merged merged--cream" rowspan="5">$19.00</td><td class="num">$38.00</td><td></td><td></td></tr>
    <tr><td class="item item--alt">Valley Silver Cedar</td><td class="size-white">100ml</td><td class="num">$38.00</td><td></td><td></td></tr>
    <tr><td class="item">Southern Shoreline</td><td class="size-white">100ml</td><td class="num">$38.00</td><td></td><td></td></tr>
    <tr><td class="item item--alt">Mountain Pepperleaf and Wild Blackcurrant</td><td class="size-white">100ml</td><td class="num">$38.00</td><td></td><td></td></tr>
    <tr><td class="item">Alpine Frost</td><td class="size-white">100ml</td><td class="num">$38.00</td><td></td><td></td></tr>
    <tr><td class="item item--alt">Wild Highland Moorland</td><td class="size-white">200ml</td><td class="merged" rowspan="5">$25.00</td><td class="num">$50.00</td><td></td><td></td></tr>
    <tr><td class="item">Valley Silver Cedar</td><td class="size-white">200ml</td><td class="num">$50.00</td><td></td><td></td></tr>
    <tr><td class="item item--alt">Southern Shoreline</td><td class="size-white">200ml</td><td class="num">$50.00</td><td></td><td></td></tr>
    <tr><td class="item">Mountain Pepperleaf and Wild Blackcurrant</td><td class="size-white">200ml</td><td class="num">$50.00</td><td></td><td></td></tr>
    <tr><td class="item item--alt">Alpine Frost</td><td class="size-white">200ml</td><td class="num">$50.00</td><td></td><td></td></tr>
    <tr><td class="item">Wild Highland Moorland, Car Diffuser</td><td class="size-white">20ml</td><td class="merged merged--cream" rowspan="2">$6.00</td><td class="num">$10.00</td><td></td><td></td></tr>
    <tr><td class="item item--alt">Mountain Pepperleaf, Car Diffuser</td><td class="size-white">20ml</td><td class="num">$10.00</td><td></td><td></td></tr>
  </table>

  <div class="section-title" style="left:110px;top:449px;width:280px">Face and body care (subject to availability)</div>
  <table class="price-table back-table" style="left:54px;top:459px">
    <colgroup><col style="width:138px"><col style="width:62px"><col style="width:44px"><col style="width:48px"><col style="width:48px"><col style="width:36px"></colgroup>
    <tr><td class="item">Magnesium Oil</td><td class="size-white">200ml (amber glass)</td><td class="num">$22.00</td><td class="num">$40.00</td><td></td><td></td></tr>
    <tr><td class="item item--alt">Face Oil</td><td class="size-white">30ml (AG)</td><td class="num">$25.00</td><td class="num">$45.00</td><td></td><td></td></tr>
    <tr><td class="item">Face Cream</td><td class="size-white">100ml (AL)</td><td class="num">$25.00</td><td class="num">$50.00</td><td></td><td></td></tr>
    <tr><td class="item item--alt">Face Mask</td><td class="size-white">10g</td><td class="num">$4.00</td><td class="num">$9.00</td><td></td><td></td></tr>
    <tr><td class="item">Hand Cream</td><td class="size-white">100ml (AG)</td><td class="num">$20.00</td><td class="num">$35.00</td><td></td><td></td></tr>
    <tr><td class="item item--alt">Lip Balm</td><td class="size-white">10g (AL)</td><td class="num">$6.00</td><td class="num">$10.00</td><td></td><td></td></tr>
    <tr><td class="item">Body Oil (lemongrass and lavender)</td><td class="size-white">250ml (AG)</td><td class="num">$22.00</td><td class="num">$40.00</td><td></td><td></td></tr>
    <tr><td class="item item--alt">Body Lotion</td><td class="size-white">250ml</td><td class="num">$22.00</td><td class="num">$40.00</td><td></td><td></td></tr>
    <tr><td class="item">Hand Wash (tranquil)</td><td class="size-white">500ml</td><td class="num">$22.00</td><td class="num">$40.00</td><td></td><td></td></tr>
  </table>

  <footer class="contact">
    <span>Please contact Nora or Tom on</span>
    <span class="phone-pill">0412 555 018</span>
    <span>or reach out to us at</span>
    <span class="mail">
      <svg width="8" height="6" viewBox="0 0 8 6" aria-hidden="true"><rect x=".5" y=".5" width="7" height="5" fill="none" stroke="#fff" stroke-width=".8"/><path d="M.5 .5 4 3.4 7.5 .5" fill="none" stroke="#fff" stroke-width=".8"/></svg>
      hello@larkfieldseedhouse.co
    </span>
  </footer>
</section>

</body>
</html>
```